International Trading Company, 'VOLA' needs a Business Card

The company name is "VOLA" and it has own logo design.
I'd like to use its logo on this business card.
I need two side Business Card.
I'll look forward to your great design.
Thank you very much in advance.

Contact Information for Business Card

Company Name : Vola Harbor Limited
Information Example
Tobias Wrenfold
Mobile(use icon please) : 1 (555) 014-2290
Tel(use icon please) : 1 (555) 014-6835
Email(use icon please) : tobias27@volaharbor.example
Address(use icon please) : 482 Larkmoor Rd, New York, NY 10199, USA

```html
<!DOCTYPE html>
<html lang="en">
<head>
<meta charset="UTF-8">
<title>Vola Harbor Limited — Business Card</title>
<link href="https://fonts.googleapis.com/css2?family=Open+Sans:wght@400;700&family=Montserrat:wght@800&display=swap" rel="stylesheet">
<style>
  :root {
    --stage: #e4e4e4;
    --card: #ffffff;
    --panel: #5e5e5e;
    --ink: #555555;
    --ink-soft: #6a6a6a;
    --logo-dark: #555555;
    --logo-light: #ffffff;
    --pattern-a: #f7f7f7;
    --pattern-b: #ececec;
  }
  * { box-sizing: border-box; margin: 0; padding: 0; }
  html, body { width: 1200px; height: 900px; overflow: hidden; }
  body {
    background: var(--stage);
    font-family: "Open Sans", Arial, sans-serif;
    display: flex;
    flex-direction: column;
    align-items: center;
    justify-content: center;
    gap: 50px;
  }
  .card {
    position: relative;
    width: 630px;
    height: 360px;
    background: var(--card);
    box-shadow: 0 6px 18px rgba(0,0,0,0.18);
    overflow: hidden;
  }
  .front-pattern {
    position: absolute;
    inset: 0;
    background: linear-gradient(135deg, var(--pattern-a), var(--pattern-b) 50%, var(--pattern-a));
  }
  .logo-word {
    font-family: "Montserrat", Arial, sans-serif;
    font-weight: 800;
    letter-spacing: 2px;
    line-height: 1;
  }
  .front .logo-word {
    position: absolute;
    left: 50%;
    top: 50%;
    transform: translate(-50%, -50%);
    font-size: 84px;
    color: var(--logo-dark);
  }
  .back-panel { position: absolute; inset: 0; }
  .back .logo-word {
    position: absolute;
    left: 60px;
    top: 150px;
    font-size: 64px;
    color: var(--logo-light);
  }
  .contact {
    position: absolute;
    right: 28px;
    top: 78px;
    text-align: right;
    color: var(--ink-soft);
    font-size: 13.5px;
    line-height: 1.45;
  }
  .contact-name {
    font-weight: 700;
    font-size: 17px;
    color: var(--ink);
    letter-spacing: 0.3px;
  }
  .contact-role {
    font-size: 13px;
    margin-bottom: 14px;
    letter-spacing: 0.3px;
  }
  .contact-row {
    display: flex;
    justify-content: flex-end;
    align-items: flex-start;
    gap: 8px;
  }
  .contact-row .icon {
    width: 12px;
    height: 12px;
    margin-top: 4px;
    flex: none;
    fill: var(--ink);
  }
  .contact-row .icon-spacer { width: 12px; flex: none; }
</style>
</head>
<body>

  <section class="card front">
    <div class="front-pattern" role="img" aria-label="Faint repeating light-grey letter pattern covering the card"></div>
    <div class="logo-word">VOLA</div>
  </section>

  <section class="card back">
    <svg class="back-panel" viewBox="0 0 630 360" aria-hidden="true">
      <polygon points="0,0 290,0 390,360 0,360" fill="var(--panel)"/>
    </svg>
    <div class="logo-word">VOLA</div>

    <div class="contact">
      <div class="contact-name">TOBIAS WRENFOLD</div>
      <div class="contact-role">CEO/FOUNDER</div>

      <div class="contact-row">
        <span>482 Larkmoor Rd, New York</span>
        <svg class="icon" viewBox="0 0 12 12"><path d="M6 0a4 4 0 0 0-4 4c0 3 4 8 4 8s4-5 4-8a4 4 0 0 0-4-4zm0 5.6A1.6 1.6 0 1 1 6 2.4a1.6 1.6 0 0 1 0 3.2z"/></svg>
      </div>
      <div class="contact-row">
        <span>NY 10199, USA</span>
        <span class="icon-spacer"></span>
      </div>
      <div class="contact-row">
        <span>1 (555) 014-6835</span>
        <svg class="icon" viewBox="0 0 12 12"><path d="M1 3.5C1 2 3 1 6 1s5 1 5 2.5V5H8.5V3.8h-5V5H1zM2.5 6h7l1.5 5H1zM6 7.2a1.5 1.5 0 1 0 0 3 1.5 1.5 0 0 0 0-3z"/></svg>
      </div>
      <div class="contact-row">
        <span>1 (555) 014-2290</span>
        <svg class="icon" viewBox="0 0 12 12"><path d="M3.5 0h5A1 1 0 0 1 9.5 1v10a1 1 0 0 1-1 1h-5a1 1 0 0 1-1-1V1a1 1 0 0 1 1-1zm.3 1.5v7.5h4.4V1.5zM6 9.8a.7.7 0 1 0 0 1.4.7.7 0 0 0 0-1.4z"/></svg>
      </div>
      <div class="contact-row">
        <span>tobias27@volaharbor.example</span>
        <svg class="icon" viewBox="0 0 12 12"><path d="M0 2h12v1L6 7 0 3zm0 2.3l6 4 6-4V10H0z"/></svg>
      </div>
      <div class="contact-row">
        <span>www.volaharbor.example</span>
        <svg class="icon" viewBox="0 0 12 12"><circle cx="6" cy="6" r="5.5"/><path d="M.5 6h11M6 .5c-2.2 2.8-2.2 8.2 0 11M6 .5c2.2 2.8 2.2 8.2 0 11" stroke="#fff" stroke-width="0.9" fill="none"/></svg>
      </div>
    </div>
  </section>

</body>
</html>
```